Jewellery Shop of 20 over years needs a new Business Card

We need a new business card that is refreshing, trendy for our Jewellery shop. We carry mid to high end fine jewellery. We want the design of the new business card to be clean cut, refreshing and different. Please try to keep to using the same logo we have, and for more information on the company you can check us out on www.tolvarjewels.com.sg or on https://www.facebook.com/Tolvarjewelworks/

Target Market(s)

late 20s to 50s

Industry/Entity Type

Jewelry Store

Contact Information for Business Card

Tolvar's Jewel Works Co Pte Ltd
517 Kestrel Avenue, #02-14/15 Marwick Plaza Singapore 249913
Tel: (65) 64721958 Fax:( 65) 64721947 WhatsApp: ( 65) 90364158
Email: tolvarhoe@quillnet.com.sg
Website: www.tolvarjewels.com.sg

Tolvar Hoe
Gemologist/Designer/Founder since 1980

Font styles to use
Serif

Requirements
Must have
• Trendy, Classic Clean Look
Should not have
• Should not be too dull or old looking, should not look like my old business card, no photos of jewellery

```html
<!DOCTYPE html>
<html lang="en">
<head>
<meta charset="utf-8">
<title>Tolvar's Jewel Works – Business Card</title>
<link href="https://fonts.googleapis.com/css2?family=Lato:wght@400;700&display=swap" rel="stylesheet">
<style>
  :root {
    --backdrop: #2b2b2b;
    --gold: #b8995a;
    --gold-light: #d2b877;
    --gold-dark: #a98c50;
    --card-white: #ffffff;
    --card-shade: #ececec;
    --ink: #2a2a2a;
    --on-gold: #ffffff;
  }
  * { box-sizing: border-box; margin: 0; padding: 0; }
  html, body {
    width: 1200px;
    height: 997px;
    overflow: hidden;
    background: var(--backdrop);
    font-family: "Lato", Arial, sans-serif;
  }
  .canvas {
    position: relative;
    width: 1200px;
    height: 997px;
  }
  .card {
    position: absolute;
    width: 560px;
    height: 320px;
    border-radius: 22px;
    box-shadow: 0 14px 40px rgba(0,0,0,.55);
    overflow: hidden;
  }
  /* Front side */
  .card-front {
    left: 90px;
    top: 110px;
    background: linear-gradient(135deg, var(--gold-light) 0%, var(--gold) 55%, var(--gold-dark) 100%);
    display: flex;
    align-items: center;
    justify-content: center;
  }
  .front-brand {
    color: var(--on-gold);
    font-weight: 700;
    font-size: 38px;
    letter-spacing: 1px;
  }
  /* Back side */
  .card-back {
    left: 550px;
    top: 540px;
    background: linear-gradient(160deg, var(--card-white) 40%, var(--card-shade) 100%);
  }
  .back-brand {
    position: absolute;
    right: 36px;
    top: 28px;
    color: var(--gold);
    font-weight: 700;
    font-size: 17px;
  }
  .divider {
    position: absolute;
    left: 220px;
    right: 34px;
    top: 140px;
    height: 2px;
    background: var(--gold);
  }
  .person {
    position: absolute;
    left: 36px;
    top: 126px;
  }
  .person-name {
    color: var(--gold);
    font-weight: 700;
    font-size: 21px;
    line-height: 1.1;
  }
  .person-role {
    color: var(--ink);
    font-weight: 700;
    font-size: 14px;
    margin-top: 2px;
  }
  .website {
    position: absolute;
    right: 36px;
    top: 168px;
    color: var(--gold);
    font-size: 16px;
    letter-spacing: .3px;
  }
  .contacts {
    position: absolute;
    left: 36px;
    top: 206px;
    list-style: none;
  }
  .contacts li {
    display: flex;
    align-items: center;
    gap: 12px;
    height: 32px;
    color: var(--ink);
    font-size: 16px;
  }
  .contact-icon {
    width: 20px;
    height: 20px;
    flex: none;
  }
</style>
</head>
<body>
<main class="canvas">

  <section class="card card-front" aria-label="Business card front">
    <span class="front-brand">Tolvar's Jewel Works</span>
  </section>

  <section class="card card-back" aria-label="Business card back">
    <span class="back-brand">Tolvar's Jewel Works</span>
    <div class="divider"></div>

    <div class="person">
      <p class="person-name">Tolvar Hoe</p>
      <p class="person-role">Gemologist &amp; Designer</p>
    </div>

    <p class="website">www.quillnet.com.sg</p>

    <ul class="contacts">
      <li>
        <svg class="contact-icon" viewBox="0 0 20 20" aria-hidden="true">
          <circle cx="10" cy="10" r="10" fill="var(--gold)"/>
          <rect x="7" y="5" width="6" height="10" rx="1.2" fill="none" stroke="#fff" stroke-width="1.4"/>
        </svg>
        +65 6472 1958
      </li>
      <li>
        <svg class="contact-icon" viewBox="0 0 20 20" aria-hidden="true">
          <circle cx="10" cy="10" r="10" fill="var(--gold)"/>
          <rect x="5" y="6.5" width="10" height="7" fill="none" stroke="#fff" stroke-width="1.3"/>
          <path d="M5 6.5 L10 10.5 L15 6.5" fill="none" stroke="#fff" stroke-width="1.3"/>
        </svg>
        +65 6472 1947
      </li>
      <li>
        <svg class="contact-icon" viewBox="0 0 20 20" aria-hidden="true">
          <circle cx="10" cy="10" r="10" fill="var(--gold)"/>
          <rect x="4.5" y="9" width="6" height="3.4" rx="1.7" transform="rotate(-45 7.5 10.7)" fill="none" stroke="#fff" stroke-width="1.3"/>
          <rect x="9.5" y="7.6" width="6" height="3.4" rx="1.7" transform="rotate(-45 12.5 9.3)" fill="none" stroke="#fff" stroke-width="1.3"/>
        </svg>
        tolvarhoe@quillnet.com.sg
      </li>
    </ul>
  </section>

</main>
</body>
</html>
```